Corvane Bookkeeping Services business cards

looking for a double sided business card design. My logo is attached. I am looking for a design similar to the attached. Keen to see what my logo in white on the blue background would look like.

```html
<!DOCTYPE html>
<html lang="en">
<head>
<meta charset="utf-8">
<title>Corvane Bookkeeping Services – Business Cards</title>
<link rel="stylesheet" href="https://fonts.googleapis.com/css2?family=Montserrat:wght@400;500;700&display=swap">
<style>
  :root {
    --navy: #1d3577;
    --navy-deep: #1a2f6e;
    --navy-soft: #243f8e;
    --green: #93bd3a;
    --ink: #1e2a44;
    --paper: #ffffff;
    --backdrop: #3b3431;
  }
  * { box-sizing: border-box; margin: 0; padding: 0; }
  html, body { width: 1200px; height: 786px; overflow: hidden; }
  body {
    background: var(--backdrop);
    font-family: "Montserrat", sans-serif;
    position: relative;
  }
  .card {
    position: absolute;
    top: 238px;
    width: 540px;
    height: 309px;
    overflow: hidden;
    box-shadow: 0 10px 30px rgba(0,0,0,.45);
  }
  /* Front */
  .card-front { left: 40px; background: var(--paper); }
  .brand {
    position: absolute;
    top: 42px;
    right: 34px;
    display: flex;
    align-items: center;
    gap: 10px;
  }
  .brand-mark { width: 26px; height: 26px; background: var(--green); }
  .brand-name {
    font-weight: 700;
    font-size: 19px;
    color: var(--navy);
    line-height: 1.1;
  }
  .brand-name span { display: block; font-size: 10.5px; letter-spacing: .08em; text-transform: uppercase; }
  .rule-top {
    position: absolute; top: 104px; left: 210px; right: 34px;
    height: 1.5px; background: var(--navy);
  }
  .person { position: absolute; left: 34px; top: 150px; }
  .person-name { font-weight: 700; font-size: 19px; color: var(--navy); }
  .person-role { font-size: 11px; color: var(--ink); margin-top: 2px; }
  .rule-person { width: 200px; height: 1.5px; background: var(--navy); margin-top: 6px; }
  .contacts { list-style: none; margin-top: 8px; }
  .contacts li {
    display: flex; align-items: center; gap: 10px;
    font-size: 11.5px; color: var(--ink); height: 17px;
  }
  .contacts svg { width: 11px; height: 11px; fill: var(--green); flex: none; }
  .address {
    position: absolute; right: 34px; top: 212px;
    font-size: 11px; line-height: 1.45; color: var(--ink); text-align: left;
  }
  .band-navy {
    position: absolute; left: 0; bottom: 0; width: 335px; height: 14px;
    background: var(--navy);
  }
  .band-green {
    position: absolute; left: 335px; right: 0; bottom: 0; height: 22px;
    background: var(--green);
  }
  /* Back */
  .card-back { left: 620px; background: var(--navy); }
  .back-pattern {
    position: absolute; inset: 0;
    background: linear-gradient(135deg, var(--navy-soft), var(--navy-deep));
  }
  .back-brand {
    position: absolute; top: 50%; left: 50%;
    transform: translate(-50%, -50%);
    display: flex; align-items: center; gap: 10px;
  }
  .back-brand .brand-mark { background: var(--paper); }
  .back-brand .brand-name { color: var(--paper); }
</style>
</head>
<body>
  <section class="card card-front" aria-label="Business card front">
    <div class="brand">
      <div class="brand-mark"></div>
      <div class="brand-name">Corvane<span>Bookkeeping Services</span></div>
    </div>
    <div class="rule-top"></div>

    <div class="person">
      <p class="person-name">Rafael Ostrin</p>
      <p class="person-role">Owner</p>
      <div class="rule-person"></div>
      <ul class="contacts">
        <li><svg viewBox="0 0 24 24"><path d="M6.6 10.8a15 15 0 0 0 6.6 6.6l2.2-2.2a1 1 0 0 1 1-.25 11 11 0 0 0 3.6.6 1 1 0 0 1 1 1V20a1 1 0 0 1-1 1A17 17 0 0 1 3 4a1 1 0 0 1 1-1h3.5a1 1 0 0 1 1 1 11 11 0 0 0 .6 3.6 1 1 0 0 1-.25 1z"/></svg>(555) 214-3071</li>
        <li><svg viewBox="0 0 24 24"><path d="M7 1h10a2 2 0 0 1 2 2v18a2 2 0 0 1-2 2H7a2 2 0 0 1-2-2V3a2 2 0 0 1 2-2zm0 3v14h10V4zm5 15.5a1 1 0 1 0 0 2 1 1 0 0 0 0-2z"/></svg>(555) 382-6640</li>
        <li><svg viewBox="0 0 24 24"><path d="M2 5h20v14H2zm2 2v.5l8 5 8-5V7l-8 5z"/></svg>info@corvanebooks.com</li>
        <li><svg viewBox="0 0 24 24"><circle cx="12" cy="12" r="10"/></svg>www.corvanebooks.com</li>
      </ul>
    </div>

    <p class="address">480 Alder Ridge Road, Ste 210<br>Millbrook, TN 37012</p>

    <div class="band-navy"></div>
    <div class="band-green"></div>
  </section>

  <section class="card card-back" aria-label="Business card back">
    <div class="back-pattern" role="img" aria-label="Tone-on-tone repeating brand pattern across the blue background"></div>
    <div class="back-brand">
      <div class="brand-mark"></div>
      <div class="brand-name">Corvane<span>Bookkeeping Services</span></div>
    </div>
  </section>
</body>
</html>
```